Velmora Solutions Website Design

We are a B2B startup offering a free virtual data room and deal management platform for small businesses. We need a 10-page website geared towards business executives and entrepreneurs that is simple, uploads quickly and provides a good introduction to our product. We've attached a document setting forth the text of 8 of the 10 pages (the other two - Resources and Blog - need to be designed to allow the future posting of white papers and blog entries) and links to the screenshots and GIFs, all of which are in a folder on dropbox. We've also attached a zip file with our logo and a pdf file with our font and colors. Examples of websites we like include www.tarnwick.example, www.plovebar.example and https://brimlo.example.

Target Market(s)

Small business owners, business executives and entrepreneurs

Industry/Entity Type

Finance

Coding

Coded - Design and coding required

Number of Pages Required

5+ page

Font styles to use
Sans Serif

Colors
85abd2
f9ba93

Requirements
Must have
• Please use the Wordpress kestle theme I uploaded to code the site.
Nice to have
• Clean, uncluttered design. White background. Screenshots and gifs should be shown on monitors (desktop, laptop and iPad only). Blue and orange are our corporate colors, but you’re not limited to those two colors. See uploaded logo guide for complementary colors or use your own judgment.

```html
<!DOCTYPE html>
<html lang="en">
<head>
<meta charset="utf-8">
<title>Velmora — Manage Your Workflow</title>
<link href="https://fonts.googleapis.com/css2?family=Roboto:wght@300;400;500;700&display=swap" rel="stylesheet">
<style>
:root{
  --blue:#4c7189;
  --blue-dark:#3f6178;
  --orange:#e8760f;
  --ink:#4a4a4a;
  --muted:#7a7a7a;
  --band:#e2e3ea;
  --cream:#fde9d3;
  --white:#ffffff;
}
*{box-sizing:border-box;margin:0;padding:0}
html,body{width:1200px;height:2988px;overflow:hidden}
body{font-family:'Roboto',sans-serif;font-weight:300;color:var(--ink);background:var(--white);position:relative}
.abs{position:absolute}
.hero-bg{left:0;top:0;width:1200px;height:470px}
.nav{left:0;top:0;width:1200px;height:90px}
.brand{left:84px;top:22px;font-size:32px;font-weight:700;color:var(--white)}
.nav-links{left:228px;top:36px;display:flex;gap:26px;font-size:14px;font-weight:400;color:var(--white)}
.nav-links .active{color:var(--orange)}
.nav-cta{left:922px;top:30px;width:198px;height:30px;background:var(--orange);color:var(--white);font-size:13px;font-weight:400;display:flex;align-items:center;justify-content:center;letter-spacing:.3px}
.laptop{left:120px;top:118px;width:460px;height:330px;border-radius:14px 14px 4px 4px;background:linear-gradient(180deg,#d9dde1,#aeb4ba)}
.hero-copy{right:80px;top:116px;width:520px;text-align:right;color:var(--white)}
.hero-copy h1{font-weight:300;font-size:32px;line-height:40px;margin-bottom:20px}
.hero-copy p{font-size:12.5px;line-height:18px;margin-bottom:14px}
.hero-copy ul{list-style:none;font-size:12px;line-height:18px;margin-bottom:14px}
.hero-copy ul li::after{content:" »"}
.hero-copy b{font-weight:700}
.demo-btn{left:862px;top:404px;width:256px;height:42px;background:var(--orange);border-radius:10px;color:var(--white);font-size:20px;font-weight:400;display:flex;align-items:center;justify-content:center}
.features-head{left:0;top:520px;width:1200px;text-align:center}
.features-head h2{font-weight:400;font-size:34px;color:var(--orange)}
.features-head p{font-size:14px;color:var(--ink);margin-top:12px}
.feature{width:240px;text-align:center}
.feature svg{display:block;margin:0 auto 14px}
.feature h3{font-weight:400;font-size:16px;color:var(--orange);margin-bottom:12px}
.feature p{font-size:12.5px;line-height:19px;color:var(--ink)}
.quote-band{left:0;top:1134px;width:1200px;height:166px;background:var(--band)}
.qmark{font-family:'Roboto',sans-serif;font-weight:700;font-size:260px;color:#c8c9d0;line-height:1}
.quote-text{left:0;top:1170px;width:1200px;text-align:center;font-size:19px;line-height:28px;color:#3c3c3c}
.quote-src{left:0;top:1232px;width:1200px;text-align:center;font-size:10.5px;color:var(--muted)}
.shot{border:1px solid #d0d4d8;box-shadow:0 10px 18px rgba(0,0,0,.12);background:linear-gradient(180deg,#f4f6f8,#e6eaee)}
.row-copy{width:400px}
.row-copy h2{font-weight:300;font-size:31px;color:#3c3c3c;padding-bottom:12px;border-bottom:1px solid var(--orange);margin-bottom:22px}
.row-copy p{font-size:13px;line-height:19px;color:var(--ink)}
.row-copy.right{text-align:right}
.row-copy.right p{padding-left:180px}
.row-copy.left p{padding-right:120px}
.cta-band{left:0;top:2456px;width:1200px;height:206px;background:var(--cream);text-align:center}
.cta-band h2{font-weight:300;font-size:30px;color:#3c3c3c;margin-top:38px}
.cta-band p{font-size:14px;margin-top:4px}
.cta-btn{display:inline-flex;align-items:center;justify-content:center;margin-top:18px;width:296px;height:44px;border-radius:22px;background:var(--blue);color:var(--white);font-size:20px;font-weight:400;letter-spacing:.5px}
.footer{left:0;top:2662px;width:1200px;height:254px;background:var(--blue)}
.foot-brand{left:156px;top:2712px;font-size:40px;font-weight:700;color:var(--white)}
.foot-about{left:156px;top:2774px;width:300px;font-size:12.5px;line-height:20px;color:#c4d4de}
.foot-col h4{font-weight:400;font-size:14px;color:var(--white);letter-spacing:.8px;margin-bottom:16px}
.foot-col ul{list-style:none;font-size:13px;color:#c4d4de}
.foot-col li{height:26px;display:flex;align-items:flex-start;gap:8px}
.foot-col li .dot{color:var(--orange)}
.foot-col .ico{width:14px;flex:0 0 14px;margin-top:2px}
.bottom-bar{left:0;top:2916px;width:1200px;height:72px;background:var(--orange);color:var(--white);font-size:14px;font-weight:400}
.bottom-bar .legal{position:absolute;left:84px;top:26px}
.social{position:absolute;right:80px;top:20px;display:flex;gap:10px}
.social span{width:30px;height:30px;border-radius:50%;background:var(--white)}
</style>
</head>
<body>

<svg class="abs hero-bg" viewBox="0 0 1200 470" aria-hidden="true">
  <path d="M0 0H1200V396Q1200 420 1176 424L720 468H0Z" fill="var(--blue)"/>
  <rect x="0" y="420" width="720" height="50" fill="#ffffff"/>
  <path d="M0 0H1200V396Q1200 420 1176 424L720 468L600 470V380Q600 300 0 300Z" fill="var(--blue)"/>
</svg>

<header class="abs nav">
  <div class="abs brand">Velmora</div>
  <nav class="abs nav-links">
    <span>Home</span><span>Features</span><span class="active">Our Clients</span><span>Company</span><span>Contact Us</span>
  </nav>
  <div class="abs nav-cta">TRY IT NOW BUTTON</div>
</header>

<div class="abs laptop" role="img" aria-label="Laptop displaying the Velmora workflow dashboard"></div>

<section class="abs hero-copy">
  <h1>Manage Your Workflow<br>Better with Velmora</h1>
  <p>The Velmora Assistant is a secure, sharable workflow<br>management platform designed with your needs<br>in mind. Here are some features you'll love:</p>
  <ul>
    <li>Built for internal and external collaboration</li>
    <li>Highly customizable and intuitive</li>
    <li>Free to use – no setup or monthly fees</li>
  </ul>
  <p>If you want to process contracts faster while reducing costs<br>(did we mention that it was free?), <b>Velmora</b> is the ideal solution for you.</p>
</section>
<div class="abs demo-btn">WATCH DEMO</div>

<section class="abs features-head">
  <h2>Features At-a-Glance</h2>
  <p>User-friendly workflow management software that saves time and money</p>
</section>

<!-- feature grid -->
<div class="abs feature" style="left:192px;top:632px">
  <svg width="64" height="62" viewBox="0 0 64 62"><polygon points="32,3 40,23 61,23 44,36 50,58 32,45 14,58 20,36 3,23 24,23" fill="none" stroke="var(--blue)" stroke-width="3" stroke-linejoin="round"/></svg>
  <h3>Workflow Management</h3>
  <p>Efficiently handle multi-party<br>transactions with<br>customizable, collaborative<br>workflow software.</p>
</div>
<div class="abs feature" style="left:482px;top:632px">
  <svg width="64" height="62" viewBox="0 0 64 62"><polygon points="32,3 40,23 61,23 44,36 50,58 32,45 14,58 20,36 3,23 24,23" fill="none" stroke="var(--blue)" stroke-width="3" stroke-linejoin="round"/></svg>
  <h3>Workflow Management</h3>
  <p>Efficiently handle multi-party<br>transactions with<br>customizable, collaborative<br>workflow software.</p>
</div>
<div class="abs feature" style="left:772px;top:632px">
  <svg width="64" height="62" viewBox="0 0 64 62"><polygon points="32,3 40,23 61,23 44,36 50,58 32,45 14,58 20,36 3,23 24,23" fill="none" stroke="var(--blue)" stroke-width="3" stroke-linejoin="round"/></svg>
  <h3>Workflow Management</h3>
  <p>Efficiently handle multi-party<br>transactions with<br>customizable, collaborative<br>workflow software.</p>
</div>
<div class="abs feature" style="left:192px;top:854px">
  <svg width="64" height="62" viewBox="0 0 64 62"><polygon points="32,3 40,23 61,23 44,36 50,58 32,45 14,58 20,36 3,23 24,23" fill="none" stroke="var(--blue)" stroke-width="3" stroke-linejoin="round"/></svg>
  <h3>Workflow Management</h3>
  <p>Efficiently handle multi-party<br>transactions with<br>customizable, collaborative<br>workflow software.</p>
</div>
<div class="abs feature" style="left:482px;top:854px">
  <svg width="64" height="62" viewBox="0 0 64 62"><polygon points="32,3 40,23 61,23 44,36 50,58 32,45 14,58 20,36 3,23 24,23" fill="none" stroke="var(--blue)" stroke-width="3" stroke-linejoin="round"/></svg>
  <h3>Workflow Management</h3>
  <p>Efficiently handle multi-party<br>transactions with<br>customizable, collaborative<br>workflow software.</p>
</div>
<div class="abs feature" style="left:772px;top:854px">
  <svg width="64" height="62" viewBox="0 0 64 62"><polygon points="32,3 40,23 61,23 44,36 50,58 32,45 14,58 20,36 3,23 24,23" fill="none" stroke="var(--blue)" stroke-width="3" stroke-linejoin="round"/></svg>
  <h3>Workflow Management</h3>
  <p>Efficiently handle multi-party<br>transactions with<br>customizable, collaborative<br>workflow software.</p>
</div>

<div class="abs quote-band"></div>
<div class="abs qmark" style="left:104px;top:1064px">“</div>
<div class="abs qmark" style="left:960px;top:1212px">”</div>
<p class="abs quote-text">"Efficient workflow management has resulted in an 85% savings<br>in deal closings over the past six years."</p>
<p class="abs quote-src">- The Global Council for Contract Operations -</p>

<div class="abs shot" style="left:96px;top:1360px;width:564px;height:336px" role="img" aria-label="Screenshot of the Velmora document workspace"></div>
<section class="abs row-copy right" style="left:722px;top:1416px">
  <h2>Waste Less, Do More</h2>
  <p>Reduce administrative costs by streamlining workflows and automating document storage and sharing from a single, cloud-based platform.</p>
</section>

<div class="abs shot" style="left:570px;top:1732px;width:568px;height:250px" role="img" aria-label="Screenshot of the Velmora deal dashboard"></div>
<section class="abs row-copy left" style="left:100px;top:1790px">
  <h2>Waste Less, Do More</h2>
  <p>Reduce administrative costs by streamlining workflows and automating document storage and sharing from a single, cloud-based platform.</p>
</section>

<div class="abs shot" style="left:96px;top:2100px;width:564px;height:256px" role="img" aria-label="Screenshot of the Velmora file sharing view"></div>
<section class="abs row-copy right" style="left:722px;top:2152px">
  <h2>Waste Less, Do More</h2>
  <p>Reduce administrative costs by streamlining workflows and automating document storage and sharing from a single, cloud-based platform.</p>
</section>

<section class="abs cta-band">
  <h2>Manage Your Workflow with Velmora</h2>
  <p>Try it today. You'll wonder how you got by without it.</p>
  <div class="cta-btn">TRY IT NOW BUTTON</div>
</section>

<footer class="abs footer"></footer>
<div class="abs foot-brand">Velmora</div>
<p class="abs foot-about">Simplify workflow management with Velmora –free business process management software built for collaboration and easy customization. Try it today!</p>
<div class="abs foot-col" style="left:506px;top:2716px">
  <h4>USEFUL LINKS</h4>
  <ul>
    <li><span class="dot">»</span>Home</li>
    <li><span class="dot">»</span>Features</li>
    <li><span class="dot">»</span>Our Clients</li>
    <li><span class="dot">»</span>Company</li>
    <li><span class="dot">»</span>Contact Us</li>
  </ul>
</div>
<div class="abs foot-col" style="left:762px;top:2716px">
  <h4>OUR CONTACTS</h4>
  <ul>
    <li style="height:52px"><svg class="ico" viewBox="0 0 14 14"><path d="M7 1a4 4 0 0 0-4 4c0 3 4 8 4 8s4-5 4-8a4 4 0 0 0-4-4z" fill="var(--orange)"/><circle cx="7" cy="5" r="1.5" fill="var(--blue)"/></svg><span>1122, Any City, Any Street<br>Any Country, 14256</span></li>
    <li><svg class="ico" viewBox="0 0 14 14"><path d="M3 1l3 3-2 2c1 2 2 3 4 4l2-2 3 3-2 2C6 13 1 8 1 3z" fill="var(--orange)"/></svg><span>+00 - 555 010 4477</span></li>
    <li><svg class="ico" viewBox="0 0 14 14"><rect x="1" y="3" width="12" height="8" fill="var(--orange)"/><path d="M1 3l6 5 6-5" fill="none" stroke="var(--blue)"/></svg><span>contact@velmorasolutions.example</span></li>
  </ul>
</div>

<div class="abs bottom-bar">
  <span class="legal">Copyrights © 2014 All Rights Reserved &nbsp;| &nbsp;&nbsp;Terms of Use / Privacy Policy</span>
  <div class="social"><span></span><span></span><span></span><span></span></div>
</div>

</body>
</html>
```